MediDesk 4.2 is web based clinic management software. We require 1 logo for the software product, login page design and landing page (patient queue) design. The design should include all elements required logo, icons , buttons and type faces. http://md2021.tralvonix.my/Default.aspxTest login : KQ417 password : 4826 Final output should be in psd for developer to convert to css for web application.

Number of Pages Required

1 page

Colors

Designer to choose colors to be used in the design.

Requirements
Must have
• Product Logo , icon, login page design, and 1 main page design as attached.

```html
<!DOCTYPE html>
<html lang="en">
<head>
<meta charset="utf-8">
<title>MediDesk 4.2 – Login and Queue</title>
<link href="https://fonts.googleapis.com/css2?family=Lato:wght@400;700;900&family=Ubuntu:wght@500;700&display=swap" rel="stylesheet">
<style>
:root{
  --navy:#1d3a5c;
  --navy-2:#24486f;
  --blue:#3a77b3;
  --teal:#2cc4c9;
  --teal-2:#4fd0c9;
  --link:#2aa8dd;
  --ink:#222;
  --muted:#888;
  --line:#e4e7ea;
  --white:#fff;
  --page:#f4f5f7;
}
*{box-sizing:border-box;margin:0;padding:0}
html,body{width:873px;height:1200px;overflow:hidden}
body{position:relative;font-family:"Lato",sans-serif;color:var(--ink);background:var(--white)}
.abs{position:absolute}
.header{left:0;top:0;width:873px;height:125px;background:var(--white);text-align:center}
.brand-name{font-family:"Lato",sans-serif;font-weight:900;color:var(--blue);letter-spacing:.5px}
.brand-tag{font-size:13px;color:#333}
.stage{left:0;top:125px;width:873px;height:1075px;background:linear-gradient(160deg,#1da6d3 0%,#1b8fc9 45%,#1d7ec4 70%,#1b6fbf 100%)}
.stage-photo{left:0;top:125px;width:873px;height:490px;background:radial-gradient(ellipse at 50% 50%,rgba(255,255,255,.08),rgba(255,255,255,0) 70%)}

/* login */
.login{left:153px;top:210px;width:567px;height:322px;border-radius:8px;overflow:hidden;background:var(--white)}
.login-promo{left:0;top:0;width:282px;height:322px;background:linear-gradient(160deg,#2a4f78,#1f4470 60%,#24507e)}
.promo-title{right:40px;top:50px;text-align:right;color:var(--white);font-family:"Ubuntu",sans-serif;font-weight:700;font-size:22px;line-height:24px}
.promo-title small{font-size:11px;color:var(--teal-2);margin-right:4px}
.promo-mark{left:0;width:282px;top:190px;text-align:center;font-size:22px}
.promo-mark .brand-name{color:var(--teal-2)}
.promo-text{left:0;width:282px;top:251px;text-align:center;color:var(--white);font-size:9px;line-height:11.5px}
.promo-mail{left:0;width:282px;top:289px;text-align:center;color:var(--teal-2);font-size:9px}
.login-form{left:282px;top:0;width:285px;height:322px}
.form-brand{left:48px;top:30px}
.form-brand .brand-name{font-size:22px;display:block}
.form-brand .brand-tag{font-size:10px;margin-top:2px}
.form-hint{left:48px;top:89px;width:150px;font-size:9px;line-height:11.5px;color:var(--muted)}
.field{left:48px;width:187px;height:30px;border:1px solid #dcdfe3;border-radius:15px;font-size:9px;color:#555;padding:0 15px;display:flex;align-items:center;justify-content:space-between}
.field svg{width:8px;height:8px;fill:#aaa}
.btn-login{left:48px;top:220px;width:100px;height:30px;border-radius:15px;background:linear-gradient(90deg,#2a4f78,#2cb6c6);color:var(--white);font-size:8px;font-weight:900;letter-spacing:1.2px;display:flex;align-items:center;justify-content:space-between;padding:0 18px}
.btn-clear{left:163px;top:231px;font-size:8px;font-weight:700;letter-spacing:1px;color:var(--link);text-decoration:underline}
.form-links{left:48px;top:297px;font-size:7.5px;color:var(--muted)}
.form-links span{margin-right:18px}

/* dashboard */
.app{left:35px;top:654px;width:802px;height:509px;border-radius:9px;overflow:hidden;background:var(--page)}
.sidebar{left:0;top:0;width:155px;height:509px;background:var(--navy)}
.side-brand{left:0;width:155px;top:20px;text-align:center}
.side-brand .brand-name{font-size:13px;color:#5fa6da}
.side-brand .brand-tag{font-size:5.5px;color:var(--white)}
.avatar{left:55px;top:64px;width:44px;height:44px;border-radius:50%;border:2px solid #5fa6da;background:radial-gradient(circle at 50% 45%,#c79a7c,#6d4e3d)}
.doc-name{left:0;width:155px;top:116px;text-align:center;color:var(--white);font-size:7.5px}
.menu{left:0;width:155px;color:var(--white);font-size:8.5px}
.menu li{list-style:none;height:27px;line-height:27px;padding-left:31px;position:relative}
.menu li.active{background:var(--navy-2)}
.menu li.active::before{content:"≡";position:absolute;left:17px}
.menu .group{color:var(--link)}
.menu .chev{position:absolute;right:28px;color:var(--white)}
.rule{left:0;width:155px;height:1px;background:#2c4b70}
.main-title{left:171px;top:28px;font-size:18px;font-weight:400}
.new-queue{left:276px;top:37px;font-size:8.5px;font-weight:700;color:var(--link);text-decoration:underline}
.user-mail{left:605px;top:37px;font-size:8.5px;color:#333}
.btn-logout{left:691px;top:29px;width:80px;height:23px;border-radius:12px;background:var(--teal);color:var(--white);font-size:7.5px;font-weight:900;letter-spacing:1px;display:flex;align-items:center;justify-content:space-between;padding:0 15px}
.flabel{top:79px;font-size:8px;color:#333}
.pill{top:84px;height:23px;border-radius:12px;color:var(--white);font-size:7.5px;display:flex;align-items:center;justify-content:space-between;padding:0 15px}
.pill.teal{background:var(--teal-2)}
.pill.navy{background:var(--navy-2)}
.tabs{left:177px;top:146px;width:608px;height:27px;border-bottom:1px solid var(--line);font-size:8.5px;font-weight:700}
.tab{top:0;height:27px;line-height:27px;padding:0 16px}
.tab.on{background:var(--white);color:var(--link)}
.tab.off{color:#444;left:100px}
.thead{left:177px;top:189px;font-size:7.5px;color:#333;width:608px}
.row{left:175px;width:610px;height:37px;background:var(--white);border-radius:3px;font-size:7.5px;color:#333;box-shadow:0 1px 2px rgba(0,0,0,.04)}
.cell{top:0;height:37px;line-height:37px}
.ico{display:inline-block;width:10px;height:10px;vertical-align:middle;margin-right:3px;stroke:#222;fill:none;stroke-width:1.2}
.pager{left:177px;top:452px;font-size:7.5px;color:#333}
.pager .dim{color:var(--muted);margin-left:18px}
.pager b{font-weight:400;margin-left:6px}
</style>
</head>
<body>
<svg width="0" height="0" style="position:absolute">
  <symbol id="i-user" viewBox="0 0 10 10"><circle cx="5" cy="3" r="2"/><path d="M1 9.5c0-2.5 2-3.5 4-3.5s4 1 4 3.5z"/></symbol>
  <symbol id="i-hand" viewBox="0 0 10 10"><path d="M3 9.5h4l1-3V4H7V2H6v2V1H5v3V2H4v4L2.5 5 2 6z"/></symbol>
  <symbol id="i-cash" viewBox="0 0 12 10"><rect x=".8" y="2" width="10.4" height="6"/><circle cx="6" cy="5" r="1.6"/></symbol>
  <symbol id="i-doc" viewBox="0 0 10 10"><path d="M2 .8h4.5L8.5 3v6.2H2z"/><path d="M4 5h2.5M4 7h2.5"/></symbol>
  <symbol id="i-phone" viewBox="0 0 10 10"><rect x="2" y=".8" width="6" height="8.4" rx=".8"/><path d="M4.3 7.8h1.4"/></symbol>
  <symbol id="i-glass" viewBox="0 0 10 10"><path d="M2 .8h6M2 9.2h6M3 .8c0 3 4 3 4 4.2S3 6.2 3 9.2M7 .8c0 3-4 3-4 4.2s4 1.2 4 4.2"/></symbol>
  <symbol id="i-clock" viewBox="0 0 10 10"><circle cx="5" cy="5" r="4.2"/><path d="M5 2.5V5l1.8 1.2"/></symbol>
  <symbol id="i-edit" viewBox="0 0 10 10"><path d="M7 1H1v8h8V4"/><path d="M4 6l.4-1.6L8.5.5l1 1-4 4z"/></symbol>
  <symbol id="i-doctor" viewBox="0 0 10 10"><circle cx="5" cy="2.8" r="2"/><path d="M1 9.5c0-2.6 1.8-3.6 4-3.6s4 1 4 3.6z"/></symbol>
</svg>

<header class="abs header">
  <div style="padding-top:44px"><span class="brand-name" style="font-size:32px">MediDesk</span></div>
  <div class="brand-tag">Management Software.</div>
</header>

<div class="abs stage"></div>
<div class="abs stage-photo" role="img" aria-label="Faint photo backdrop of a stethoscope and laptop on a desk"></div>

<section class="abs login">
  <div class="abs login-promo" role="img" aria-label="Dark blue photo of a stethoscope on a laptop">
    <div class="abs promo-title"><small>Web based</small>Clinic<br>management<br>software</div>
    <div class="abs promo-mark"><span class="brand-name">MediDesk</span></div>
    <p class="abs promo-text">MediDesk 4.2 is web based clinic<br>management software.</p>
    <p class="abs promo-mail">info@tralvonix.my</p>
  </div>
  <div class="abs login-form">
    <div class="abs form-brand"><span class="brand-name">MediDesk</span><span class="brand-tag">Management Software.</span></div>
    <p class="abs form-hint">Please enter your username and password to login.</p>
    <div class="abs field" style="top:132px">Username<svg viewBox="0 0 10 10"><circle cx="5" cy="3" r="2.2"/><path d="M.5 10c0-3 2-4 4.5-4s4.5 1 4.5 4z"/></svg></div>
    <div class="abs field" style="top:176px">Password<svg viewBox="0 0 10 10"><rect x="1.5" y="4.5" width="7" height="5.5" rx=".8"/><path d="M3 4.5V3a2 2 0 014 0v1.5" fill="none" stroke="#aaa" stroke-width="1.2"/></svg></div>
    <div class="abs btn-login">LOGIN <span>→</span></div>
    <div class="abs btn-clear">CLEAR</div>
    <div class="abs form-links"><span>Forgot your login?</span><span>Privacy Policy</span></div>
  </div>
</section>

<section class="abs app">
  <aside class="abs sidebar">
    <div class="abs side-brand"><span class="brand-name">MediDesk</span><br><span class="brand-tag">Management Software.</span></div>
    <div class="abs avatar" role="img" aria-label="Doctor profile photo"></div>
    <p class="abs doc-name">DR. Name Goes Here</p>
    <ul class="abs menu" style="top:155px">
      <li class="active">Queue</li><li>Patient</li><li>Visit Entry</li><li>Payment</li>
    </ul>
    <div class="abs rule" style="top:278px"></div>
    <ul class="abs menu" style="top:290px">
      <li class="group">Claims Invoice<span class="chev">⌄</span></li><li>Standard</li><li>Wizard-style</li><li>Bulk</li><li>Flat</li>
    </ul>
    <div class="abs rule" style="top:441px"></div>
    <ul class="abs menu" style="top:453px"><li class="group">Maintenance<span class="chev">›</span></li></ul>
  </aside>

  <h1 class="abs main-title">Queue List</h1>
  <span class="abs new-queue">New Queue</span>
  <span class="abs user-mail">info@tralvonix.my</span>
  <div class="abs btn-logout">LOGOUT <span>→</span></div>

  <span class="abs flabel" style="left:175px;top:92px">Show</span>
  <div class="abs pill teal" style="left:211px;top:84px;width:79px">All Status <span>⌄</span></div>
  <span class="abs flabel" style="left:316px;top:92px">From</span>
  <div class="abs pill navy" style="left:348px;width:95px">19 Nov 2018 <span>⌄</span></div>
  <span class="abs flabel" style="left:471px;top:92px">to</span>
  <div class="abs pill navy" style="left:490px;width:96px">19 Nov 2018 <span>⌄</span></div>
  <span class="abs flabel" style="left:607px;top:92px">Location</span>
  <div class="abs pill navy" style="left:651px;width:80px">All Facilities <span>⌄</span></div>

  <div class="abs tabs">
    <div class="abs tab on" style="left:0">New Patient</div>
    <div class="abs tab off">Existing Patient</div>
  </div>

  <div class="abs thead">
    <span class="abs" style="left:8px">No</span>
    <span class="abs" style="left:120px">Patient Name</span>
    <span class="abs" style="left:284px">Time</span>
    <span class="abs" style="left:339px">Payor</span>
    <span class="abs" style="left:377px">Amount</span>
    <span class="abs" style="left:435px">Doctor</span>
    <span class="abs" style="left:485px">Location</span>
  </div>

  <div class="abs row" style="top:208px">
    <span class="abs cell" style="left:10px">01</span>
    <span class="abs cell" style="left:37px"><svg class="ico"><use href="#i-user"/></svg><svg class="ico"><use href="#i-hand"/></svg><svg class="ico" style="width:12px"><use href="#i-cash"/></svg><svg class="ico"><use href="#i-doc"/></svg></span>
    <span class="abs cell" style="left:123px">Dummy Name</span>
    <span class="abs cell" style="left:198px">26 ♂</span>
    <span class="abs cell" style="left:251px">10:40 AM</span>
    <span class="abs cell" style="left:306px"><svg class="ico"><use href="#i-phone"/></svg></span>
    <span class="abs cell" style="left:344px">RM 2,473.12</span>
    <span class="abs cell" style="left:402px">000178</span>
    <span class="abs cell" style="left:452px">-</span>
    <span class="abs cell" style="left:508px"><svg class="ico" style="margin-right:10px"><use href="#i-glass"/></svg><svg class="ico" style="margin-right:10px"><use href="#i-clock"/></svg><svg class="ico" style="margin-right:10px"><use href="#i-edit"/></svg><svg class="ico"><use href="#i-doctor"/></svg></span>
  </div>
  <div class="abs row" style="top:252px">
    <span class="abs cell" style="left:10px">02</span>
    <span class="abs cell" style="left:37px"><svg class="ico"><use href="#i-user"/></svg><svg class="ico"><use href="#i-hand"/></svg><svg class="ico" style="width:12px"><use href="#i-cash"/></svg><svg class="ico"><use href="#i-doc"/></svg></span>
    <span class="abs cell" style="left:123px">Dummy Name</span>
    <span class="abs cell" style="left:198px">26 ♂</span>
    <span class="abs cell" style="left:251px">10:40 AM</span>
    <span class="abs cell" style="left:306px"><svg class="ico"><use href="#i-phone"/></svg></span>
    <span class="abs cell" style="left:344px">RM 2,473.12</span>
    <span class="abs cell" style="left:402px">000178</span>
    <span class="abs cell" style="left:452px">-</span>
    <span class="abs cell" style="left:508px"><svg class="ico" style="margin-right:10px"><use href="#i-glass"/></svg><svg class="ico" style="margin-right:10px"><use href="#i-clock"/></svg><svg class="ico" style="margin-right:10px"><use href="#i-edit"/></svg><svg class="ico"><use href="#i-doctor"/></svg></span>
  </div>
  <div class="abs row" style="top:296px">
    <span class="abs cell" style="left:10px">03</span>
    <span class="abs cell" style="left:37px"><svg class="ico"><use href="#i-user"/></svg><svg class="ico"><use href="#i-hand"/></svg><svg class="ico" style="width:12px"><use href="#i-cash"/></svg><svg class="ico"><use href="#i-doc"/></svg></span>
    <span class="abs cell" style="left:123px">Dummy Name</span>
    <span class="abs cell" style="left:198px">26 ♂</span>
    <span class="abs cell" style="left:251px">10:40 AM</span>
    <span class="abs cell" style="left:306px"><svg class="ico"><use href="#i-phone"/></svg></span>
    <span class="abs cell" style="left:344px">RM 2,473.12</span>
    <span class="abs cell" style="left:402px">000178</span>
    <span class="abs cell" style="left:452px">-</span>
    <span class="abs cell" style="left:508px"><svg class="ico" style="margin-right:10px"><use href="#i-glass"/></svg><svg class="ico" style="margin-right:10px"><use href="#i-clock"/></svg><svg class="ico" style="margin-right:10px"><use href="#i-edit"/></svg><svg class="ico"><use href="#i-doctor"/></svg></span>
  </div>
  <div class="abs row" style="top:340px">
    <span class="abs cell" style="left:10px">04</span>
    <span class="abs cell" style="left:37px"><svg class="ico"><use href="#i-user"/></svg><svg class="ico"><use href="#i-hand"/></svg><svg class="ico" style="width:12px"><use href="#i-cash"/></svg><svg class="ico"><use href="#i-doc"/></svg></span>
    <span class="abs cell" style="left:123px">Dummy Name</span>
    <span class="abs cell" style="left:198px">26 ♂</span>
    <span class="abs cell" style="left:251px">10:40 AM</span>
    <span class="abs cell" style="left:306px"><svg class="ico"><use href="#i-phone"/></svg></span>
    <span class="abs cell" style="left:344px">RM 2,473.12</span>
    <span class="abs cell" style="left:402px">000178</span>
    <span class="abs cell" style="left:452px">-</span>
    <span class="abs cell" style="left:508px"><svg class="ico" style="margin-right:10px"><use href="#i-glass"/></svg><svg class="ico" style="margin-right:10px"><use href="#i-clock"/></svg><svg class="ico" style="margin-right:10px"><use href="#i-edit"/></svg><svg class="ico"><use href="#i-doctor"/></svg></span>
  </div>
  <div class="abs row" style="top:384px">
    <span class="abs cell" style="left:10px">05</span>
    <span class="abs cell" style="left:37px"><svg class="ico"><use href="#i-user"/></svg><svg class="ico"><use href="#i-hand"/></svg><svg class="ico" style="width:12px"><use href="#i-cash"/></svg><svg class="ico"><use href="#i-doc"/></svg></span>
    <span class="abs cell" style="left:123px">Dummy Name</span>
    <span class="abs cell" style="left:198px">26 ♂</span>
    <span class="abs cell" style="left:251px">10:40 AM</span>
    <span class="abs cell" style="left:306px"><svg class="ico"><use href="#i-phone"/></svg></span>
    <span class="abs cell" style="left:344px">RM 2,473.12</span>
    <span class="abs cell" style="left:402px">000178</span>
    <span class="abs cell" style="left:452px">-</span>
    <span class="abs cell" style="left:508px"><svg class="ico" style="margin-right:10px"><use href="#i-glass"/></svg><svg class="ico" style="margin-right:10px"><use href="#i-clock"/></svg><svg class="ico" style="margin-right:10px"><use href="#i-edit"/></svg><svg class="ico"><use href="#i-doctor"/></svg></span>
  </div>

  <div class="abs pager">Page 1 of 4<span class="dim">Prev</span><b>1</b><b>2</b><b>3</b><b>4</b><b>Next</b></div>
</section>
</body>
</html>
```